Business Card Design for Small Electrical Contractor

I need to update my business card into something a little more modern. We are a small electrical contracting company. We service domestic and commercial places around Sydney. We have 2 logo designs at the moment. I have uploaded both and 2 different sizes to work with.

Industry/Entity Type

Business

Contact Information for Business Card

Ted Corbin
8/21-23 Holt St, Fernhaven 2087
t - (02) 9471 3820
m - 0427 915 304
E - info@corbinelec.example.au
W - corbinelec.example.au
ABN: 42 907 518 263

Font styles to use
Sans Serif

Requirements
Must have
• I would also like to see the below fit on somewhere aswell
• - Licensed Electrician
• - Level 2 (Cat 1 & 4)
• - Domestic
• - Commercial
• - Repairs and Installations
• - Data
Nice to have
• Try and keep similar colours as logo
Should not have
• No lightning bolts or light globes. Smart and professional please.

```html
<!DOCTYPE html>
<html lang="en">
<head>
<meta charset="utf-8">
<title>T&amp;R Corbin Electrical – Business Cards</title>
<link rel="stylesheet" href="https://fonts.googleapis.com/css2?family=Montserrat:wght@400;500;600;700&display=swap">
<style>
  :root {
    --backdrop: #2b2b2d;
    --card: #ffffff;
    --green: #0f3d36;
    --orange: #f39a1e;
    --ink: #1d2b28;
  }
  * { box-sizing: border-box; margin: 0; padding: 0; }
  html, body { width: 1200px; height: 900px; overflow: hidden; }
  body {
    background: var(--backdrop);
    font-family: "Montserrat", sans-serif;
    color: var(--ink);
    position: relative;
  }
  .card {
    position: absolute;
    width: 540px;
    height: 310px;
    background: var(--card);
    border-radius: 22px;
    overflow: hidden;
    box-shadow: 0 14px 30px rgba(0,0,0,.45);
  }
  .card--front { left: 70px; top: 90px; }
  .card--back { left: 590px; top: 500px; }
  .card__shapes { position: absolute; inset: 0; width: 100%; height: 100%; }

  .brand-name {
    position: absolute;
    font-weight: 600;
    font-size: 27px;
    line-height: 1.1;
    color: var(--green);
    letter-spacing: .5px;
  }
  .card--front .brand-name { right: 36px; top: 42px; text-align: right; }
  .card--back .brand-name { left: 36px; top: 40px; }

  .services {
    position: absolute;
    left: 34px; top: 128px;
    list-style: none;
    font-size: 13.5px;
    line-height: 1.28;
    color: var(--ink);
  }
  .services li::before {
    content: "";
    display: inline-block;
    width: 5px; height: 5px;
    border-radius: 50%;
    background: var(--orange);
    margin: 0 9px 2px 0;
  }
  .website-band {
    position: absolute;
    left: 34px; bottom: 16px;
    color: #fff;
    font-size: 15px;
    font-weight: 500;
    letter-spacing: .3px;
  }

  .person {
    position: absolute;
    right: 32px; top: 46px;
    text-align: right;
    width: 240px;
  }
  .person__name {
    font-size: 24px;
    font-weight: 600;
    color: var(--green);
    padding-bottom: 6px;
    border-bottom: 1.5px solid var(--green);
  }
  .person__name .first { color: var(--orange); font-weight: 500; }
  .person__address {
    margin-top: 8px;
    font-size: 13px;
    line-height: 1.4;
  }
  .abn {
    position: absolute;
    right: 16px; top: 252px;
    color: #fff;
    font-size: 13px;
    white-space: nowrap;
  }
  .abn .label { color: var(--orange); }

  .contacts {
    position: absolute;
    left: 36px; top: 172px;
    width: 320px;
    border-top: 1.5px solid var(--green);
    padding-top: 8px;
    list-style: none;
    font-size: 14px;
    line-height: 1.3;
  }
  .contacts li { display: flex; align-items: center; gap: 10px; }
  .contacts svg { width: 11px; height: 11px; flex: none; }
  .contacts .accent { color: var(--orange); }
</style>
</head>
<body>

<section class="card card--front" aria-label="Business card, services side">
  <svg class="card__shapes" viewBox="0 0 540 310" aria-hidden="true">
    <polygon points="0,262 250,262 300,282 300,310 0,310" fill="var(--green)"/>
    <polygon points="300,282 540,240 540,256 300,298" fill="var(--orange)"/>
  </svg>
  <div class="brand-name">T&amp;R Corbin<br>Electrical</div>
  <ul class="services">
    <li>Licensed Electrician</li>
    <li>Level 2 (Cat 1 &amp; 4)</li>
    <li>Domestic</li>
    <li>Commercial</li>
    <li>Repairs and Installations</li>
    <li>Data</li>
  </ul>
  <div class="website-band">www.corbinelec.example.au</div>
</section>

<section class="card card--back" aria-label="Business card, contact side">
  <svg class="card__shapes" viewBox="0 0 540 310" aria-hidden="true">
    <polygon points="372,222 540,222 540,310 358,310" fill="var(--green)"/>
    <polygon points="0,296 366,264 363,278 0,310" fill="var(--orange)"/>
  </svg>
  <div class="brand-name">T&amp;R Corbin<br>Electrical</div>

  <div class="person">
    <div class="person__name"><span class="first">Ted</span> Corbin</div>
    <div class="person__address">8/21-23 Holt St<br>Fernhaven 2087</div>
  </div>
  <div class="abn"><span class="label">ABN:</span> 42 907 518 263</div>

  <ul class="contacts">
    <li>
      <svg viewBox="0 0 12 12"><path d="M2 1h3l1 3-1.5 1a6 6 0 0 0 2.5 2.5L8 6l3 1v3a1 1 0 0 1-1 1A9 9 0 0 1 1 2a1 1 0 0 1 1-1z" fill="var(--orange)"/></svg>
      (02) 9471 3820
    </li>
    <li>
      <svg viewBox="0 0 12 12"><rect x="3" y="0.5" width="6" height="11" rx="1.2" fill="none" stroke="var(--orange)" stroke-width="1.3"/></svg>
      0427 915 304
    </li>
    <li>
      <svg viewBox="0 0 12 12"><rect x="0.7" y="2" width="10.6" height="8" fill="none" stroke="var(--orange)" stroke-width="1.2"/><path d="M1 2.5l5 4 5-4" fill="none" stroke="var(--orange)" stroke-width="1.2"/></svg>
      info@corbinelec.example.au
    </li>
    <li>
      <svg viewBox="0 0 12 12"><circle cx="6" cy="6" r="5" fill="none" stroke="var(--orange)" stroke-width="1.2"/><ellipse cx="6" cy="6" rx="2.2" ry="5" fill="none" stroke="var(--orange)" stroke-width="1"/><path d="M1 6h10" stroke="var(--orange)" stroke-width="1"/></svg>
      <span>www.<span class="accent">corbinelec</span>.example.au</span>
    </li>
  </ul>
</section>

</body>
</html>
```